Letterhead to coordinate with business card

I am needing a docx template and print file for a letterhead to co-ordinate with my newly designed logo and business card.

```html
<!DOCTYPE html>
<html lang="en">
<head>
<meta charset="utf-8">
<title>Harbour Plan Services – Letterhead</title>
<link href="https://fonts.googleapis.com/css2?family=Montserrat:ital,wght@0,400;0,600;1,400&family=Roboto+Condensed:wght@700&display=swap" rel="stylesheet">
<style>
  :root{
    --backdrop:#e4e4e2;
    --paper:#ffffff;
    --navy:#2f3440;
    --magenta:#a8306a;
    --teal:#00a89b;
    --ink:#3a3a3a;
    --ink-strong:#2f2f2f;
  }
  *{box-sizing:border-box;margin:0;padding:0}
  html,body{width:1200px;height:1200px;overflow:hidden;background:var(--backdrop)}
  .letterhead{
    position:absolute;left:167px;top:40px;width:865px;height:1120px;
    background:var(--paper);overflow:hidden;
    box-shadow:0 2px 10px rgba(0,0,0,.12);
    font-family:"Montserrat",sans-serif;color:var(--ink);
  }
  .corner-art{position:absolute;width:300px;height:220px}
  .corner-art--top{left:0;top:0}
  .corner-art--bottom{right:0;bottom:0}
  .brand{
    position:absolute;left:614px;top:48px;width:209px;
    display:flex;flex-direction:column;align-items:center;gap:16px;
  }
  .brand-square{width:66px;height:66px;background:var(--teal)}
  .brand-name{
    font-weight:600;font-size:19px;
    color:var(--magenta);text-align:center;line-height:1.25;
  }
  .date{position:absolute;left:115px;top:293px;font-weight:600;font-size:15.5px;color:var(--ink-strong)}
  .recipient{position:absolute;left:115px;top:352px;font-size:15.3px;line-height:21.5px}
  .recipient .name{font-weight:600;color:var(--ink-strong)}
  .recipient .role{font-style:italic}
  .body-copy{position:absolute;left:115px;top:459px;width:625px;font-size:15.3px;line-height:23.8px}
  .body-copy p{margin-bottom:18px}
  .sign-off{position:absolute;left:600px;top:805px;width:151px;text-align:right;font-size:15.3px}
  .signature{position:absolute;left:609px;top:832px;width:142px;height:44px;
    background:linear-gradient(90deg,#ececec,#f6f6f6);border-radius:4px}
  .signer{position:absolute;left:620px;top:878px;width:131px;font-weight:600;font-size:15.5px;color:var(--ink-strong)}
  .contact-list{position:absolute;left:33px;top:1000px;list-style:none}
  .contact-list li{display:flex;align-items:center;height:26.3px;
    font-family:"Roboto Condensed",sans-serif;font-weight:700;font-size:11.5px;color:var(--ink-strong)}
  .contact-list svg{width:16px;height:16px;margin-right:8px;flex:none}
</style>
</head>
<body>
<main class="letterhead">
  <svg class="corner-art corner-art--top" viewBox="0 0 300 220" role="img" aria-label="Decorative corner graphic in navy, teal and magenta">
    <defs>
      <linearGradient id="cornerWash" x1="0" y1="0" x2="1" y2="1">
        <stop offset="0" stop-color="var(--navy)"/>
        <stop offset=".55" stop-color="var(--teal)"/>
        <stop offset="1" stop-color="var(--magenta)"/>
      </linearGradient>
    </defs>
    <path d="M0 0H300A300 220 0 0 1 0 220Z" fill="url(#cornerWash)"/>
  </svg>

  <svg class="corner-art corner-art--bottom" viewBox="0 0 300 220" role="img" aria-label="Decorative corner graphic in navy, teal and magenta">
    <defs>
      <linearGradient id="cornerWashLow" x1="1" y1="1" x2="0" y2="0">
        <stop offset="0" stop-color="var(--navy)"/>
        <stop offset=".55" stop-color="var(--teal)"/>
        <stop offset="1" stop-color="var(--magenta)"/>
      </linearGradient>
    </defs>
    <path d="M300 220H0A300 220 0 0 1 300 0Z" fill="url(#cornerWashLow)"/>
  </svg>

  <div class="brand">
    <span class="brand-square"></span>
    <span class="brand-name">Harbour Plan Services</span>
  </div>

  <p class="date">Date, 22 February 2022</p>

  <div class="recipient">
    <p>To:</p>
    <p class="name">Liam Carter</p>
    <p class="role">Chief Officer</p>
  </div>

  <div class="body-copy">
    <p>Lorem ipsum dolor sit amet, consectetur adipiscing elit. Duis auctor sem vel metus interdum porta. Duis consequat bibendum felis eget cursus. Nulla eget purus vehicula ipsum finibus egestas. Nullam ligula ipsum, mollis sed gravida vitae, maximus eu dolor. Morbi luctus sem a congue consectetur.</p>
    <p>Orci varius natoque penatibus et magnis dis parturient montes, nascetur ridiculus mus. Vestibulum congue eros auctor, ullamcorper libero blandit, tempor tellus. Proin vitae tellus et nunc fringilla lacinia. Sed augue erat, facilisis laoreet velit a, convallis mattis nunc. Nunc sagittis ligula vitae sollicitudin sollicitudin.</p>
    <p>Nulla facilisi. Nulla quis odio vitae purus aliquam fermentum ut nec diam. Fusce sed velit ultrices, aliquam augue ut, sollicitudin orci.</p>
  </div>

  <p class="sign-off">Kind Regards</p>
  <div class="signature" role="img" aria-label="Handwritten signature of the sender"></div>
  <p class="signer">Liam Carter</p>

  <ul class="contact-list">
    <li>
      <svg viewBox="0 0 16 16"><circle cx="8" cy="8" r="8" fill="var(--teal)"/><rect x="5.5" y="3.5" width="5" height="9" rx="1" fill="none" stroke="#fff" stroke-width="1.2"/></svg>
      0412 555 304
    </li>
    <li>
      <svg viewBox="0 0 16 16"><circle cx="8" cy="8" r="8" fill="var(--teal)"/><rect x="4" y="5" width="8" height="6" fill="none" stroke="#fff" stroke-width="1.1"/><path d="M4 5l4 3.2L12 5" fill="none" stroke="#fff" stroke-width="1.1"/></svg>
      info@harbourplanservices.com.au
    </li>
    <li>
      <svg viewBox="0 0 16 16"><circle cx="8" cy="8" r="8" fill="var(--teal)"/><circle cx="8" cy="8" r="4.2" fill="none" stroke="#fff" stroke-width="1"/><path d="M3.8 8h8.4M8 3.8v8.4M8 3.8q-2.5 4.2 0 8.4M8 3.8q2.5 4.2 0 8.4" fill="none" stroke="#fff" stroke-width=".8"/></svg>
      www.harbourplanservices.com.au
    </li>
    <li>
      <svg viewBox="0 0 16 16"><path d="M8 0.5a6 6 0 0 0-6 6c0 4.5 6 9 6 9s6-4.5 6-9a6 6 0 0 0-6-6z" fill="var(--teal)"/><circle cx="8" cy="6.5" r="2.2" fill="#fff"/></svg>
      PO Box 240, Kellybrook NSW 2299
    </li>
  </ul>
</main>
</body>
</html>
```